NetProfile background/title banner

Feel free to visit my website (kvbhomecheck.ca) and current NetProfile (KVB Property Inspections) page for a general feel. We focus on our trades background and experience. I have uploaded some logos that I would like used here. We offer Commercial, Residential, Agricultural inspections. With 24/7 online booking and call center.
Updates
Please ensure the small logos are added. Try to use all 3 colors. Red, Grey, Black (and some white), leave room for the profile pic that appear in the bottom left as well.
Target Market(s)
realtors and real estate professionals
Industry/Entity Type
Property Inspections for Real Estate
Logo Text
"Inspected by Tradesmen"
Font styles to use
Requirements
Must have
- To be simple with the key highlights and logos.

```html
<!DOCTYPE html>
<html lang="en">
<head>
<meta charset="utf-8">
<title>KVB Property Inspections – Inspected by Tradesmen</title>
<link rel="stylesheet" href="https://fonts.googleapis.com/css2?family=Open+Sans:wght@400;600;700;800&display=swap">
<style>
  :root {
    --red: #f2000c;
    --red-deep: #d8121c;
    --red-soft: #e32a31;
    --white: #ffffff;
  }
  * { margin: 0; padding: 0; box-sizing: border-box; }
  html, body { width: 1200px; height: 203px; overflow: hidden; background: var(--red); }
  .banner {
    position: relative;
    width: 1200px;
    height: 203px;
    overflow: hidden;
    font-family: "Open Sans", Arial, sans-serif;
    color: var(--white);
  }
  .backdrop {
    position: absolute; inset: 0;
    background: linear-gradient(90deg, var(--red-deep) 0%, var(--red) 30%, var(--red) 60%, var(--red-soft) 100%);
  }
  .tagline {
    position: absolute; left: 49px; top: 38px;
    font-weight: 600; font-size: 21px; line-height: 27px;
    letter-spacing: 0.2px;
  }
  .checks { position: absolute; left: 36px; top: 92px; }
  .badge { position: absolute; }
  .badge-seal { left: 223px; top: 39px; width: 80px; height: 80px; }
  .badge-training { left: 324px; top: 44px; width: 53px; height: 45px; background: rgba(255,255,255,0.9); border-radius: 3px; }
  .badge-camera { left: 324px; top: 106px; width: 53px; height: 15px; background: var(--white); border-radius: 2px; }
  .badge-binder { left: 397px; top: 50px; width: 43px; height: 64px; background: rgba(255,255,255,0.9); border-radius: 5px; }
  .badge-rewards { left: 457px; top: 39px; width: 82px; height: 82px; border-radius: 50%; background: var(--white); }
  .rewards-offer {
    position: absolute; left: 247px; top: 134px; width: 268px;
    text-align: center;
  }
  .rewards-offer .headline { font-weight: 700; font-size: 13.2px; line-height: 17px; }
  .rewards-offer .fine { font-weight: 400; font-size: 10px; line-height: 15px; letter-spacing: 0.2px; }
  .title {
    position: absolute; left: 558px; top: 22px;
    font-weight: 800; font-size: 72px; line-height: 76px;
    letter-spacing: 1px;
  }
  .title .row { display: block; white-space: nowrap; }
  .title .by {
    position: absolute; left: 407px; top: 24px; width: 37px;
    border-top: 3px solid var(--white); border-bottom: 3px solid var(--white);
    font-size: 22px; line-height: 32px; text-align: center; letter-spacing: 0;
  }
  .brand {
    position: absolute; left: 1032px; top: 92px;
    font-weight: 600; font-size: 15.5px; line-height: 17px;
  }
  .brand-mark { display: block; width: 12px; height: 12px; background: var(--white); margin: 0 0 10px 56px; }
</style>
</head>
<body>
<div class="banner">
  <div class="backdrop" role="img" aria-label="Faded photo of a row of houses tinted red"></div>

  <p class="tagline">INSPECTIONS<br>AND MORE...!</p>

  <svg class="checks" width="200" height="72" viewBox="0 0 200 72" aria-hidden="true">
    <g fill="none" stroke="#ffffff" stroke-width="4">
      <rect x="7" y="31" width="33" height="34"/>
      <rect x="67" y="31" width="33" height="34"/>
      <rect x="127" y="31" width="33" height="34"/>
    </g>
    <g fill="#ffffff">
      <polygon points="12,44 22,58 70,6 72,8 22,66 8,47"/>
      <polygon points="72,44 82,58 130,6 132,8 82,66 68,47"/>
      <polygon points="132,44 142,58 190,6 192,8 142,66 128,47"/>
    </g>
  </svg>

  <svg class="badge badge-seal" viewBox="0 0 80 80" role="img" aria-label="Certification seal">
    <circle cx="40" cy="40" r="39" fill="#ffffff"/>
    <circle cx="40" cy="40" r="31" fill="none" stroke="#f2000c" stroke-width="1.2"/>
  </svg>
  <div class="badge badge-training" role="img" aria-label="Training certification badge"></div>
  <div class="badge badge-camera" role="img" aria-label="Thermal camera partner badge"></div>
  <div class="badge badge-binder" role="img" aria-label="Home records partner badge"></div>
  <div class="badge badge-rewards" role="img" aria-label="Rewards programme badge"></div>

  <div class="rewards-offer">
    <p class="headline">WE OFFER SKYPOINTS® REWARD POINTS*</p>
    <p class="fine">*Someconditions apply. Contact us for details ®</p>
  </div>

  <h1 class="title">
    <span class="row">INSPECTED</span>
    <span class="row">TRADESMEN</span>
    <span class="by">BY</span>
  </h1>

  <div class="brand">
    <span class="brand-mark"></span>
    KVB PROPERTY<br>INSPECTIONS
  </div>
</div>
</body>
</html>
```